Storm Restoration Contractor needs a professional business card design

Looking for a professional business card design. Not looking for your cheapo MS Word standard ones that are readily available. Dont want it to be cookie cutter look like ones readily available online. We just recently changed our logo and want to freshen up all our documents. Our company handles restoring a property back to a pre-loss condition after a storm damages it. For example, wind, hail, flood, fire losses.

Target Market(s)

Property Owners, Homeowners, Property Owners, Commercial Property Owners, Property Management Companies, Hail and Wind Damaged Properties

Industry/Entity Type

Construction Company

Contact Information for Business Card

Brightline Facades
847-555-0193
847-555-0147 fax
www.brightlinefacades.example
info@brightlinefacades.example

Requirements
Must have
• Clean, Professional, fresh look
• Storm Restoration, Roofing, Siding, Windows
Nice to have
• If there is a way to incorporate storms that may be cool.

```html
<!DOCTYPE html>
<html lang="en">
<head>
<meta charset="utf-8">
<title>Brightline Facades – Business Card</title>
<link href="https://fonts.googleapis.com/css2?family=Open+Sans:wght@400;600;700&display=swap" rel="stylesheet">
<style>
  :root {
    --stage: #e9eaec;
    --slate: #505051;
    --slate-dark: #3c3c3d;
    --brand-blue: #1f72bd;
    --paper: #ffffff;
    --ink-light: #ffffff;
    --shadow: rgba(0,0,0,0.18);
  }
  * { box-sizing: border-box; margin: 0; padding: 0; }
  html, body {
    width: 1200px; height: 900px; overflow: hidden;
    background: var(--stage);
    font-family: "Open Sans", Arial, sans-serif;
  }
  .canvas { position: relative; width: 1200px; height: 900px; }
  .card {
    position: absolute; left: 320px;
    width: 560px; height: 320px;
    border-radius: 18px; overflow: hidden;
    box-shadow: 0 6px 18px var(--shadow);
  }
  .brand {
    display: flex; align-items: center; gap: 10px;
    font-weight: 700; letter-spacing: 1px; text-transform: uppercase;
    white-space: nowrap;
  }
  .brand-dot { width: 26px; height: 26px; border-radius: 50%; flex: none; }

  /* Back side */
  .card-back {
    top: 100px; background: var(--slate);
    color: var(--ink-light);
    display: flex; flex-direction: column; align-items: center; justify-content: center;
    text-align: center;
  }
  .card-back .brand { font-size: 22px; margin-bottom: 24px; }
  .card-back .brand-dot { background: var(--ink-light); }
  .services { font-size: 17px; line-height: 1.5; }
  .services-url { font-size: 16px; }

  /* Front side */
  .card-front { top: 480px; background: var(--paper); display: flex; }
  .front-brand-area {
    width: 52%; height: 100%;
    display: flex; align-items: flex-start; justify-content: center;
    padding-top: 100px;
  }
  .card-front .brand { font-size: 17px; color: var(--brand-blue); }
  .card-front .brand-dot { background: var(--brand-blue); }
  .front-contact {
    position: relative; width: 48%; height: 100%;
    background: var(--brand-blue); color: var(--ink-light);
    padding: 112px 12px 0 26px;
  }
  .front-contact::before {
    content: ""; position: absolute; left: 0; top: 128px; bottom: 0;
    width: 9px; background: var(--slate-dark);
  }
  .person-name { font-size: 21px; font-weight: 700; line-height: 1.2; }
  .person-title { font-size: 13px; margin-bottom: 8px; }
  .contact-list { list-style: none; font-size: 13px; line-height: 1.6; }
  .contact-list li { display: flex; align-items: center; gap: 7px; white-space: nowrap; }
  .contact-list svg { width: 14px; height: 14px; flex: none; }
</style>
</head>
<body>
<main class="canvas">
  <section class="card card-back" aria-label="Business card, back">
    <div class="brand"><span class="brand-dot"></span>Brightline Facades</div>
    <p class="services">Storm Restoration | Roofing | Siding | Windows</p>
    <p class="services-url">www.brightlinefacades.example</p>
  </section>

  <section class="card card-front" aria-label="Business card, front">
    <div class="front-brand-area">
      <div class="brand"><span class="brand-dot"></span>Brightline Facades</div>
    </div>
    <div class="front-contact">
      <p class="person-name">Daniel Marsh</p>
      <p class="person-title">Director</p>
      <ul class="contact-list">
        <li>
          <svg viewBox="0 0 16 16" aria-hidden="true"><path fill="#fff" d="M3 2h3l1 3-2 1a8 8 0 0 0 5 5l1-2 3 1v3a1 1 0 0 1-1 1A12 12 0 0 1 2 3a1 1 0 0 1 1-1z"/></svg>
          847-555-0193
        </li>
        <li>
          <svg viewBox="0 0 16 16" aria-hidden="true"><rect x="4" y="1" width="8" height="5" fill="#fff"/><rect x="1" y="6" width="14" height="6" rx="1" fill="#fff"/><rect x="4" y="10" width="8" height="5" fill="#fff" stroke="#1f72bd"/></svg>
          847-555-0147
        </li>
        <li>
          <svg viewBox="0 0 16 16" aria-hidden="true"><rect x="1" y="3" width="14" height="10" rx="1" fill="#fff"/><path d="M1 4l7 5 7-5" fill="none" stroke="#1f72bd" stroke-width="1.3"/></svg>
          info@brightlinefacades.example
        </li>
        <li>
          <svg viewBox="0 0 16 16" aria-hidden="true"><circle cx="8" cy="8" r="7" fill="#fff"/><g fill="none" stroke="#1f72bd" stroke-width="1"><ellipse cx="8" cy="8" rx="3" ry="7"/><path d="M1 8h14M2.5 4.5h11M2.5 11.5h11"/></g></svg>
          www.brightlinefacades.example
        </li>
      </ul>
    </div>
  </section>
</main>
</body>
</html>
```